VFX Company Business Card Design Project

The Ember Vale is a decentralized Visual Effects Studio servicing the television and feature film industries.
Project Brief:
Take our logo that was previously designed on Pixel Harbor and make a double sided business card.
Requirements:
- Card MUST be double sided.
- Front of card MUST have the yellow part of our logo against the dark grey background.
- Back of card is completely up to the designer.
- Back of card must include the complete company logo.
Please follow these File Preparation guidelines:
http://printmoor.example/infopage?file=filetype_en&s=PrintMoor_new&lang=en
Industry/Entity Type
Business
Look and feel
Each slider illustrates characteristics of the customer's brand and the style your logo design should communicate.

```html
<!DOCTYPE html>
<html lang="en">
<head>
<meta charset="utf-8">
<title>The Ember Vale – Business Card</title>
<link rel="stylesheet" href="https://fonts.googleapis.com/css2?family=Open+Sans:wght@400;600&display=swap">
<style>
  :root {
    --backdrop: #3b3b3b;
    --card: #262626;
    --accent: #fcc72a;
    --ink-light: #e9e9e9;
    --ink-muted: #8a9094;
    --ink-dark: #1d1d1d;
  }
  * { margin: 0; padding: 0; box-sizing: border-box; }
  html, body {
    width: 1200px; height: 900px; overflow: hidden;
    background: var(--backdrop);
    font-family: "Open Sans", Arial, sans-serif;
  }
  .canvas { position: relative; width: 1200px; height: 900px; }

  .card { position: absolute; background: var(--card); box-shadow: 0 4px 14px rgba(0,0,0,.35); overflow: hidden; }

  /* Front */
  .card--front { left: 174px; top: 291px; width: 524px; height: 299px; }
  .brand {
    position: absolute; left: 46px; top: 116px;
    display: flex; align-items: center; gap: 18px;
  }
  .brand__dot { width: 48px; height: 48px; border-radius: 50%; background: var(--accent); flex: none; }
  .brand__name {
    font-size: 46px; font-weight: 400; color: var(--ink-light);
    letter-spacing: 0.5px; line-height: 1; white-space: nowrap;
  }
  .web-band {
    position: absolute; left: 279px; top: 214px; width: 245px; height: 26px;
    background: var(--accent); color: var(--ink-dark);
    font-size: 18px; line-height: 26px; padding-left: 9px; white-space: nowrap;
  }

  /* Back */
  .card--back { left: 726px; top: 187px; width: 301px; height: 525px; }
  .pattern-field {
    position: absolute; left: 0; top: 0; width: 301px; height: 285px;
    background: linear-gradient(to bottom, #4a4a4a 0%, #363636 45%, var(--card) 100%);
  }
  .back-brand {
    position: absolute; left: 0; top: 104px; width: 301px;
    display: flex; justify-content: center; align-items: center; gap: 10px;
  }
  .back-brand__dot { width: 26px; height: 26px; border-radius: 50%; background: var(--accent); flex: none; }
  .back-brand__name {
    font-size: 27px; font-weight: 400; color: var(--ink-light);
    line-height: 1; white-space: nowrap;
  }
  .name-band {
    position: absolute; left: 90px; top: 291px; width: 211px; height: 26px;
    background: var(--accent); color: var(--ink-dark);
    font-size: 18px; line-height: 26px; padding-left: 10px; white-space: nowrap;
  }
  .job-title {
    position: absolute; right: 54px; top: 321px;
    font-size: 13px; color: var(--ink-light); white-space: nowrap;
  }
  .contact-list {
    position: absolute; right: 52px; list-style: none;
    font-size: 13px; color: var(--ink-light); text-align: right; line-height: 18px;
  }
  .contact-list--phones { top: 361px; }
  .contact-list--online { top: 420px; }
  .contact-list li { display: flex; justify-content: flex-end; align-items: center; gap: 9px; white-space: nowrap; }
  .contact-list svg { width: 9px; height: 9px; fill: var(--accent); flex: none; }
</style>
</head>
<body>
<main class="canvas">

  <section class="card card--front" aria-label="Card front">
    <div class="brand">
      <span class="brand__dot"></span>
      <span class="brand__name">The Ember Vale</span>
    </div>
    <div class="web-band">www.embervale.example</div>
  </section>

  <section class="card card--back" aria-label="Card back">
    <div class="pattern-field" role="img" aria-label="Repeating company name pattern fading downward"></div>
    <div class="back-brand">
      <span class="back-brand__dot"></span>
      <span class="back-brand__name">The Ember Vale</span>
    </div>
    <div class="name-band">Marcus Delorne</div>
    <p class="job-title">Sales Manager</p>

    <ul class="contact-list contact-list--phones">
      <li>+1 555 014 2290
        <svg viewBox="0 0 10 10" aria-label="Phone"><rect x="2" y="0" width="6" height="10" rx="1"/></svg>
      </li>
      <li>+1 555 014 2290
        <svg viewBox="0 0 10 10" aria-label="Fax"><rect x="2" y="0" width="6" height="3"/><rect x="0" y="3" width="10" height="5"/><rect x="2" y="7" width="6" height="3"/></svg>
      </li>
    </ul>

    <ul class="contact-list contact-list--online">
      <li>hello@embervale.example
        <svg viewBox="0 0 10 10" aria-label="Email"><path d="M0 2h10v6H0z M0 2l5 3.5L10 2"/></svg>
      </li>
      <li>www.embervale.example
        <svg viewBox="0 0 10 10" aria-label="Website"><circle cx="5" cy="5" r="5"/></svg>
      </li>
    </ul>
  </section>

</main>
</body>
</html>
```